Business Card Design Project

I am community manager and social media strategist. I need a double sided business card with company logo and name. Looking for something professional, elegant but also a little bit original.

• - The logo and the colours are the company colours and a required to stay.
- The size should be: 84 x 55 mm (or 3.30 x 2.16)
- The file size should be: 1039 x 697 pixels (300 dpi)
- I'd like rounded corners. :)

Use the following contact information for the card:

Léonie Vardin
Stratégie médias sociaux / community management / édition de sites sociaux
mob. : 0687529103
leonie.vardin@postelune.fr
Twitter. : @lvardin
Skype : vardin.leonie

```html
<!DOCTYPE html>
<html lang="fr">
<head>
<meta charset="utf-8">
<title>Léonie Vardin Stratégie — carte de visite</title>
<link href="https://fonts.googleapis.com/css2?family=Lato:wght@400;700&display=swap" rel="stylesheet">
<style>
  :root {
    --page-bg: #eeeeee;
    --card-bg: #ffffff;
    --card-edge: #c9c9c9;
    --title: #8b8fc6;
    --text: #6fb2d8;
    --mark: #2a6fb0;
  }
  html, body {
    margin: 0;
    padding: 0;
    width: 801px;
    height: 1200px;
    overflow: hidden;
    background: var(--page-bg);
  }
  .card {
    position: absolute;
    left: 24px;
    top: 29px;
    width: 753px;
    height: 1142px;
    box-sizing: border-box;
    background: var(--card-bg);
    border: 3px solid var(--card-edge);
    border-radius: 60px;
    box-shadow: 0 6px 14px rgba(0, 0, 0, 0.25);
    font-family: "Lato", sans-serif;
    text-align: center;
  }
  .line {
    position: absolute;
    left: 0;
    right: 0;
    margin: 0;
    line-height: 50px;
    transform: translateY(-50%);
  }
  .company {
    font-weight: 700;
    font-size: 42px;
    color: var(--title);
  }
  .contact, .service {
    font-weight: 400;
    font-size: 38px;
    color: var(--text);
  }
  .brand {
    position: absolute;
    left: 0;
    right: 0;
    top: 940px;
    display: flex;
    align-items: center;
    justify-content: center;
    gap: 18px;
    font-family: "Lato", sans-serif;
    font-weight: 700;
    font-size: 38px;
    color: var(--mark);
  }
  .brand-dot {
    width: 34px;
    height: 34px;
    border-radius: 50%;
    background: var(--mark);
  }
</style>
</head>
<body>
  <div class="card">
    <p class="line company" style="top:200px">Léonie Vardin Stratégie</p>
    <p class="line contact" style="top:267px">0687529103</p>
    <p class="line contact" style="top:317px">Twitter: @lvardin</p>
    <p class="line contact" style="top:367px">Skype: vardin.leonie</p>
    <p class="line contact" style="top:477px">leonie.vardin@postelune.fr</p>
    <p class="line service" style="top:580px">médias sociaux</p>
    <p class="line service" style="top:632px">community management</p>
    <p class="line service" style="top:685px">édition de sites sociaux</p>
    <div class="brand">
      <span class="brand-dot"></span>
      <span>Léonie Vardin</span>
    </div>
  </div>
</body>
</html>
```